Buchcover-Design für Coaching-Buch
Zielgruppe
22 Coaches (m/w/d) haben zusammen ein Buch geschrieben - mit ihren besten Tipps, Mut machenden Geschichten und Inspirationen. Herausgekommen ist 'Die stille Mentorin am Fensterbrett - 22 Schatzkisten lüften ihre Rätsel'. Zielgruppe sind vorwiegend Frauen, häufig mit spirituellem Hintergrund oder an Selbstentwicklung interessiert, sowie Menschen, die sich ermutigen lassen möchten und Menschen, die inspirierende Texte und Geschichten mögen. Die Themen sind ganz unterschiedlich, von Selbstliebe über die Wirkung von Farben, vom Überwinden von Krisen und Angst, Umgang mit Emotionen etc. pp. - ein ganzer Blumenstrauß an Themen.
Aufgabenstellung
Der Titel 'Die stille Mentorin am Fensterbrett' kam auf, weil wir die Vorstellung hatten, dass in dem Buch vielleicht abends im Bett gelesen wird und man dann ruhig schlafen kann.
Warum Füllhörner? Nun, jeder Coach hat viel zu geben. Zu jedem Text wird es ein Geschenk geben, das die Autor*innen online zur Verfügung stellen. Dies sind PDFs mit Tipps, Meditationen oder sogar eine kurze Gratis-Session. Es braucht also etwas auf dem Cover, das darauf hindeutet, vielleicht eine Plakette oder etwas Ähnliches, das 'Mit 22 Geschenken' besagt. Im Buchsatz wird dies durch einen Link (E-Book) und durch einen QR-Code (Print) umgesetzt.

```html
<!DOCTYPE html>
<html lang="de">
<head>
<meta charset="utf-8">
<title>Die stille Mentorin am Fensterbrett – Buchcover</title>
<link rel="stylesheet" href="https://fonts.googleapis.com/css2?family=Josefin+Sans:wght@200;300;600&family=Kaushan+Script&display=swap">
<style>
  :root {
    --page: #ffffff;
    --peach: #e6b7a1;
    --peach-light: #efc6b3;
    --peach-deep: #d9a58d;
    --bloom-orange: #f0a34a;
    --bloom-white: #f4eee8;
    --copper-light: #f0a060;
    --copper: #c9682c;
    --copper-dark: #8f4317;
    --white: #ffffff;
  }
  html, body {
    margin: 0;
    width: 844px;
    height: 1200px;
    overflow: hidden;
    background: var(--page);
  }
  .book-cover {
    position: absolute;
    left: 42px;
    top: 60px;
    width: 760px;
    height: 1080px;
    overflow: hidden;
    box-shadow: 4px 4px 6px rgba(0,0,0,0.45);
  }
  .cover-photo {
    position: absolute;
    inset: 0;
    background:
      radial-gradient(ellipse 260px 150px at 52% 5%, rgba(240,163,74,0.75), rgba(240,163,74,0) 100%),
      radial-gradient(ellipse 280px 120px at 62% 100%, rgba(244,238,232,0.95), rgba(244,238,232,0) 100%),
      radial-gradient(ellipse 60px 60px at 10% 86%, rgba(236,196,74,0.85), rgba(236,196,74,0) 100%),
      linear-gradient(180deg, var(--peach-light) 0%, var(--peach) 55%, var(--peach-deep) 100%);
  }
  .author-name {
    position: absolute;
    top: 68px;
    left: 0;
    width: 760px;
    text-align: center;
    font-family: "Josefin Sans", sans-serif;
    font-weight: 200;
    font-size: 54px;
    letter-spacing: 22px;
    text-indent: 22px;
    color: var(--white);
  }
  .title-kicker {
    position: absolute;
    font-family: "Josefin Sans", sans-serif;
    font-weight: 600;
    font-size: 44px;
    letter-spacing: 2px;
    color: var(--white);
    white-space: nowrap;
    transform: translateX(-50%);
  }
  .title-kicker--first { left: 336px; top: 282px; }
  .title-kicker--second { left: 503px; top: 497px; }
  .title-script {
    position: absolute;
    inset: 0;
    width: 760px;
    height: 1080px;
  }
  .title-script text {
    font-family: "Kaushan Script", cursive;
    fill: url(#copperFoil);
  }
  .subtitle {
    position: absolute;
    left: 54px;
    top: 780px;
    width: 440px;
    text-align: center;
    font-family: "Josefin Sans", sans-serif;
    font-weight: 300;
    font-size: 42px;
    line-height: 52px;
    color: var(--white);
  }
  .gift-badge {
    position: absolute;
    left: 479px;
    top: 733px;
    width: 220px;
    height: 220px;
    border-radius: 50%;
    background: radial-gradient(circle at 35% 30%, var(--copper-light), var(--copper) 55%, var(--copper-dark) 100%);
    display: flex;
    align-items: center;
    justify-content: center;
    text-align: center;
  }
  .gift-badge__text {
    font-family: "Josefin Sans", sans-serif;
    font-weight: 600;
    font-size: 21px;
    line-height: 29px;
    color: var(--white);
    transform: rotate(-5deg);
    margin-top: 6px;
  }
</style>
</head>
<body>
  <main class="book-cover">
    <div class="cover-photo" role="img" aria-label="Foto: Blüten in Orange, Weiß und Gelb auf pfirsichfarbenem Untergrund"></div>

    <p class="author-name" style="margin:0">AUTORENNAMEN</p>

    <h1 style="margin:0">
      <span class="title-kicker title-kicker--first">DIE STILLE</span>
      <svg class="title-script" viewBox="0 0 760 1080" aria-label="Mentorin … Fensterbrett">
        <defs>
          <linearGradient id="copperFoil" x1="0" y1="0" x2="1" y2="1">
            <stop offset="0" stop-color="#f2a768"/>
            <stop offset="0.45" stop-color="#c8672b"/>
            <stop offset="0.7" stop-color="#e58d4c"/>
            <stop offset="1" stop-color="#9a4a1a"/>
          </linearGradient>
        </defs>
        <text x="50" y="455" font-size="150" textLength="655" lengthAdjust="spacingAndGlyphs">Mentorin</text>
        <text x="50" y="705" font-size="118" textLength="665" lengthAdjust="spacingAndGlyphs">Fensterbrett</text>
      </svg>
      <span class="title-kicker title-kicker--second">AM</span>
    </h1>

    <p class="subtitle" style="margin:0">22 SCHATZKISTEN<br>LÜFTEN IHRE<br>RÄTSEL</p>

    <div class="gift-badge">
      <p class="gift-badge__text" style="margin:0">INKL.<br>MEDITATIONEN<br>ZAHLREICHE<br>TIPPS, &amp; GRATIS-<br>SESSION</p>
    </div>
  </main>
</body>
</html>
```